Dietitian needs awesome business card

I need a contemporary design that's eye catching but professional.
My card is to given to doctors, specialists and patients alike.
I manage patients with chronic diseases
I have uploaded my logo and current business card, I would also like the other Registered Clinical Nutritionist logo incorporated into the design

Target Market(s)

Doctors, specialists and patients

Industry/Entity Type

Healthcare

Contact Information for Business Card

www.brindlecovenutrition.com.au
Ph: 0427 516 903
Fax: 6482 7315
email: marcus.k.wellfare@quorvamail.com
Space on the back of the card with: Appointment date, Appointment time and appointment location

Font styles to use
Serif

Colors
fbee3e
876aae
ffc214

Requirements
Must have
• My Logo
• Registered Clinical Nutritionist Logo
• My 4 locations - Fernhollow Medical Centre, North Kelby Health, Ashcourt Medical, Pinebrook Doctors Surgery
Nice to have
• I like the colours in my current business card

```html
<!DOCTYPE html>
<html lang="en">
<head>
<meta charset="utf-8">
<title>Brindle Cove Nutrition – Business Card</title>
<link href="https://fonts.googleapis.com/css2?family=Vollkorn:wght@400;600&family=Josefin+Sans:wght@400&display=swap" rel="stylesheet">
<style>
  :root {
    --purple: #8a3bc9;
    --pale-yellow: #fdfd9a;
    --gold: #ffc80a;
    --white: #ffffff;
    --ink: #2b2b2b;
    --navy: #1c2a8c;
    --blue: #0a7cc4;
    --green: #3aa335;
    --lime: #9acc1a;
    --band-green: #22a33a;
  }
  * { margin: 0; padding: 0; box-sizing: border-box; }
  html, body { width: 1200px; height: 850px; overflow: hidden; background: var(--white); }
  .canvas { position: relative; width: 1200px; height: 850px; }
  .card-frame {
    position: absolute; left: 165px; top: 170px; width: 870px; height: 510px;
    background: var(--purple);
  }
  .panel { position: absolute; }
  .panel--locations { left: 183px; top: 186px; width: 307px; height: 478px; background: var(--pale-yellow); }
  .panel--middle { left: 490px; top: 186px; width: 211px; height: 204px; background: var(--white); }
  .panel--gold { left: 701px; top: 186px; width: 316px; height: 478px; background: var(--gold); }
  .card-front {
    position: absolute; left: 490px; top: 390px; width: 520px; height: 270px;
    background: var(--white); overflow: hidden;
  }
  .panel--white-foot { left: 490px; top: 660px; width: 211px; height: 4px; background: var(--white); }

  .serif { font-family: "Vollkorn", Georgia, serif; color: var(--ink); }
  .locations {
    position: absolute; left: 180px; top: 192px; width: 380px;
    font-size: 26px; line-height: 32px; letter-spacing: 0.8px;
    text-align: center; list-style: none; white-space: nowrap;
  }
  .appointment-label {
    position: absolute; left: 190px; top: 334px; width: 335px;
    font-size: 20px; line-height: 26px; font-weight: 600; text-align: center; letter-spacing: 0.8px;
  }
  .appointment-box {
    position: absolute; left: 190px; top: 402px; width: 301px; height: 254px;
    border: 3px solid var(--purple); background: var(--pale-yellow);
  }
  .appointment-arrow { position: absolute; left: 334px; top: 388px; z-index: 2; }
  .contact {
    position: absolute; left: 545px; top: 260px; width: 470px;
    font-size: 24px; line-height: 32px; letter-spacing: 0.3px;
    text-align: center; list-style: none; white-space: nowrap;
  }
  .swoosh { position: absolute; left: 0; top: 0; }
  .brand {
    position: absolute; left: 40px; top: 105px; display: flex; align-items: center; gap: 8px;
  }
  .brand__mark { width: 38px; height: 38px; border-radius: 50%; background: var(--blue); }
  .brand__name {
    font-family: "Josefin Sans", Arial, sans-serif; font-size: 24px; line-height: 26px; color: var(--navy);
  }
  .divider { position: absolute; left: 263px; top: 70px; width: 1px; height: 128px; background: #555; }
  .person {
    position: absolute; left: 281px; top: 106px;
    font-family: "Josefin Sans", Arial, sans-serif; font-size: 21px; color: var(--navy);
  }
  .person-contact {
    position: absolute; left: 277px; top: 155px; list-style: none;
    font-family: "Josefin Sans", Arial, sans-serif; font-size: 12.5px; line-height: 20px; color: #111;
  }
  .credential-band {
    position: absolute; left: 15px; top: 230px; width: 505px; height: 20px;
    background: var(--band-green); color: var(--white);
    font-family: "Josefin Sans", Arial, sans-serif; font-size: 17px; line-height: 21px; text-align: center;
  }
</style>
</head>
<body>
<div class="canvas">
  <div class="card-frame"></div>
  <div class="panel panel--locations"></div>
  <div class="panel panel--gold"></div>
  <div class="panel panel--middle"></div>

  <ul class="locations serif">
    <li>Fernhollow Medical Centre,</li>
    <li>North Kelby Health,</li>
    <li>Ashcourt Medical,</li>
    <li>Pinebrook Doctors Surgery</li>
  </ul>

  <p class="appointment-label serif">Appointment date, Appointment<br>time and appointment location</p>
  <div class="appointment-box"></div>
  <svg class="appointment-arrow" width="24" height="28" viewBox="0 0 24 28" aria-hidden="true">
    <path d="M7 0 H17 V14 H24 L12 27 L0 14 H7 Z" fill="#9acc1a"/>
  </svg>

  <ul class="contact serif">
    <li>www.brindlecovenutrition.com.au</li>
    <li>Ph: 0427 516 903</li>
    <li>Fax: 6482 7315</li>
    <li>email: marcus.k.wellfare@quorvamail.com</li>
  </ul>

  <div class="card-front">
    <svg class="swoosh" width="520" height="270" viewBox="0 0 520 270" aria-hidden="true">
      <defs>
        <linearGradient id="sky" x1="0" x2="1" y1="0" y2="0">
          <stop offset="0" stop-color="#ffffff"/>
          <stop offset="0.5" stop-color="#0a8ccc"/>
          <stop offset="1" stop-color="#0c1a7a"/>
        </linearGradient>
        <linearGradient id="leaf" x1="0" x2="1" y1="0" y2="0">
          <stop offset="0" stop-color="#3aa335"/>
          <stop offset="0.5" stop-color="#c8e01a"/>
          <stop offset="1" stop-color="#22a33a"/>
        </linearGradient>
      </defs>
      <path d="M0 0 H520 V72 C420 25 250 8 0 2 Z" fill="url(#sky)"/>
      <path d="M0 4 C250 12 420 32 520 80 V92 C420 44 250 16 0 5 Z" fill="url(#leaf)"/>
      <rect x="0" y="0" width="100" height="4" fill="#1530b8"/>
    </svg>
    <div class="brand">
      <span class="brand__mark"></span>
      <span class="brand__name">Brindle Cove<br>Nutrition</span>
    </div>
    <div class="divider"></div>
    <p class="person">Marcus Wellfare</p>
    <ul class="person-contact">
      <li>Phone: 0427 516 903</li>
      <li>email: marcus.k.wellfare@quorvamail.com</li>
    </ul>
    <p class="credential-band">Registered Clinical Nutritionist, Nutritionist and Chef</p>
  </div>
  <div class="panel panel--white-foot"></div>
</div>
</body>
</html>
```